Create look and feel for existing Web Page

Update Web Page

We have a website at http://www.usekivra.com/index-web.html. It is a single page html site, with a custom signup form. We also have a quill bay plugin at the bottom of the page. We'd like to redesign the look and feel of the entire site. We sell software to eye doctors. Also called optometrists, our software tool makes it easy for doctors to manage patients, bill, and document patient encounters. I have included our logos below.

We are looking for a new design preferably in HTML 5, CSS etc. The fields on the form on this page: http://www.usekivra.com/index-web.html

You can get screen shots of our software application at this site: http://staging.usekivra.com
username: test@samplevora.com
password: password

```html
<!DOCTYPE html>
<html lang="en">
<head>
<meta charset="utf-8">
<title>Ocravel — Practice software for eye doctors</title>
<link href="https://fonts.googleapis.com/css2?family=Roboto:wght@400;500;700;900&family=Fondamento&display=swap" rel="stylesheet">
<style>
:root{
  --ink:#0b0b0d;
  --orange:#ff8a1c;
  --white:#ffffff;
  --muted:#f3f3f3;
  --text:#222222;
  --panel:#3b404b;
  --panel-dark:#2f333c;
  --card:#3d4352;
  --blue:#1e96f0;
}
*{margin:0;padding:0;box-sizing:border-box}
html,body{width:1200px;height:818px;overflow:hidden;background:var(--white)}
body{position:relative;font-family:'Roboto',sans-serif;color:var(--text)}
.hero{position:absolute;left:0;top:0;width:1200px;height:545px;overflow:hidden;
  background:radial-gradient(ellipse 260px 190px at 560px 250px,#2b3d38 0%,#1a1f1f 45%,transparent 100%),
  radial-gradient(ellipse 700px 380px at 600px 270px,#1c1c1c 0%,#0b0b0d 75%),var(--ink)}
.hero-photo{position:absolute;inset:0}
.hero-curve{position:absolute;left:0;top:0}
.site-header{position:absolute;left:0;top:0;width:1200px;height:52px}
.brand{position:absolute;left:103px;top:15px;font-family:'Roboto',sans-serif;font-weight:500;font-size:21px;color:var(--orange);letter-spacing:1px}
.main-nav{position:absolute;left:414px;top:19px;display:flex;gap:17px}
.main-nav a{color:var(--white);text-decoration:none;font-weight:500;font-size:11.5px}
.btn{display:block;position:absolute;background:var(--orange);color:var(--white);text-decoration:none;border-radius:30px;text-align:center;font-weight:400}
.btn-signup{left:1008px;top:12px;width:92px;height:29px;line-height:29px;font-size:12px}
.hero-copy{position:absolute;left:100px;top:148px;width:400px;color:var(--white)}
.hero-copy h1{font-size:41px;font-weight:700;line-height:1.1}
.hero-copy h2{font-size:28px;font-weight:400;margin-top:8px}
.hero-copy p{font-size:11.3px;line-height:13.8px;margin-top:22px;width:395px}
.btn-chart{left:100px;top:335px;width:201px;height:29px;line-height:29px;font-size:11.5px}
.app-preview{position:absolute;left:596px;top:137px}
.about{position:absolute;left:0;top:545px;width:1200px}
.about-word{position:absolute;left:22px;top:-22px;font-size:167px;font-weight:900;color:var(--muted);letter-spacing:-3px;line-height:1}
.about h3{position:absolute;left:102px;top:106px;font-size:19px;font-weight:500;color:#1a1a1a}
.about p{position:absolute;left:100px;top:152px;width:800px;font-family:'Fondamento',cursive;font-size:18px;line-height:30px;color:#333}
</style>
</head>
<body>
<section class="hero">
  <div class="hero-photo" role="img" aria-label="Close-up photo of a human eye in dark tones"></div>
  <svg class="hero-curve" width="1200" height="545" viewBox="0 0 1200 545"><path d="M0 487 Q600 595 1200 487 L1200 545 L0 545 Z" fill="#fff"/></svg>

  <header class="site-header">
    <div class="brand">Ocravel</div>
    <nav class="main-nav">
      <a href="#">Home</a><a href="#">About</a><a href="#">Our Software</a><a href="#">Features</a><a href="#">Pricing</a><a href="#">Contact Us</a>
    </nav>
    <a class="btn btn-signup" href="#">Sign Up</a>
  </header>

  <div class="hero-copy">
    <h1>Hi Doctor</h1>
    <h2>Let us Save you time</h2>
    <p>With <b>Ocravel</b> management system you could save a massive amount of time. <b>Ocravel</b> is your office operating system. Automate your painful tasks, keep track of your books, and live a little. Start with a FREE charting tool and add more products as you grow.</p>
  </div>
  <a class="btn btn-chart" href="#">Sign Up For <b>Free</b> Charting Tool</a>

  <svg class="app-preview" width="504" height="237" viewBox="0 0 504 237" font-family="Roboto,sans-serif">
    <rect x="0" y="28" width="49" height="181" fill="var(--panel)"/>
    <text x="3" y="36" font-size="4.5" font-weight="500" fill="var(--orange)">Ocravel</text>
    <circle cx="28" cy="68" r="7" fill="#ccc"/>
    <rect x="0" y="93" width="49" height="7" fill="var(--blue)"/>
    <g font-size="2.6" fill="#ddd"><text x="11" y="82">Dashboard</text><text x="11" y="90">Calendar</text><text x="11" y="98">Search</text><text x="11" y="106">Settings</text><text x="11" y="122">Patient Engagement</text><text x="11" y="138">Logout</text></g>
    <rect x="462" y="28" width="42" height="181" fill="#fafafa"/>
    <rect x="462" y="40" width="42" height="22" fill="var(--panel)"/>
    <circle cx="492" cy="88" r="3.5" fill="var(--blue)"/>
    <rect x="462" y="102" width="30" height="4" fill="var(--blue)"/>
    <rect x="462" y="160" width="30" height="4" fill="var(--blue)"/>
    <rect x="462" y="201" width="42" height="8" fill="var(--panel-dark)"/>
    <rect x="49" y="0" width="413" height="237" fill="#f7f7f7"/>
    <rect x="49" y="0" width="73" height="237" fill="var(--panel)"/>
    <text x="53" y="10" font-size="6" font-weight="500" fill="var(--orange)">Ocravel</text>
    <text x="85" y="27" font-size="3.4" fill="#fff" text-anchor="middle">Alex Reed</text>
    <text x="85" y="33" font-size="2.4" fill="#ccc" text-anchor="middle">test@samplevora.com</text>
    <circle cx="85" cy="45" r="9" fill="#d6d6d6"/>
    <rect x="49" y="64" width="70" height="8" rx="3" fill="var(--blue)"/>
    <g font-size="3.4" fill="#eee"><text x="62" y="70">Dashboard</text><text x="62" y="81">Calendar</text><text x="62" y="91">Search</text><text x="62" y="102">Settings</text><text x="62" y="112">Patient Engagement</text><text x="62" y="123">Logout</text></g>
    <rect x="122" y="0" width="340" height="17" fill="#fff"/>
    <text x="127" y="11" font-size="5.5" fill="#333" font-weight="500">Mara's LLC</text>
    <text x="128" y="28" font-size="4.2" fill="#555">Total Patient's Chart : 3</text>
    <line x1="130" y1="98" x2="458" y2="98" stroke="#ccc" stroke-width=".5"/>
    <line x1="130" y1="42" x2="130" y2="98" stroke="#ccc" stroke-width=".5"/>
    <path d="M130 98 L265 98 Q272 98 276 70 Q279 42 281 42 Q283 42 286 70 Q290 98 296 98 L345 98 Q350 96 353 85 Q357 70 359 70 Q362 72 366 88 Q369 98 374 98 L458 98 Z" fill="var(--card)"/>
    <g font-size="5" fill="#fff">
      <rect x="126" y="114" width="105" height="54" fill="var(--card)"/>
      <text x="130" y="123">Sales Revenue</text><text x="130" y="129" font-size="2.5" fill="#bbb">Lifetime sales total</text>
      <text x="130" y="149" font-size="12">5000</text>
      <rect x="240" y="114" width="104" height="54" fill="var(--card)"/>
      <text x="244" y="123">Cash Revenue</text><text x="244" y="129" font-size="2.5" fill="#bbb">Lifetime sales total</text>
      <text x="244" y="149" font-size="12">5000</text>
      <rect x="353" y="114" width="104" height="54" fill="var(--card)"/>
      <text x="357" y="123">Credit Card Revenue</text><text x="357" y="129" font-size="2.5" fill="#bbb">Lifetime sales total</text>
      <text x="357" y="149" font-size="12">0</text>
    </g>
    <rect x="126" y="185" width="331" height="35" fill="#fff"/>
    <text x="130" y="198" font-size="5" fill="#444">Schedule</text>
    <rect x="280" y="191" width="53" height="8" fill="var(--card)"/>
    <g font-size="2.8" fill="#888"><text x="132" y="214">Patient</text><text x="275" y="214">Appointment Time</text><text x="355" y="214">Status</text><text x="410" y="214">Confirmation</text></g>
    <rect x="122" y="221" width="340" height="16" fill="var(--panel-dark)"/>
    <text x="456" y="231" font-size="3" fill="#ddd" text-anchor="end">© Ocravel 2019. All rights reserved</text>
  </svg>
</section>

<section class="about">
  <div class="about-word" aria-hidden="true">About</div>
  <h3>How We Are</h3>
  <p>We are lease doctors who got tired of the administration associated with running a lease practice, so instead of complaining we created a system to do it all for us.</p>
</section>
</body>
</html>
```